Website design with eCommerce for revolutionary new product in the manufacturing industry.

We need a website designed for a precision manufacturing company based in the suburbs of Minneapolis, Minnesota called Velk Manufacturing. We have a revolutionary new product, the TREMLA, to introduce and sell through an eCommerce storefront. The website would include company information, product information, and the storefront. Green is a color that represents Velk Manufacturing. The final design should communicate that we exclusively offer premium products at a premium price. The design should also let the customer know they are the focus of our work.

Target Market(s)

Machinists and machine shops

Industry/Entity Type

Manufacturing and machine shops

Coding

Coded - Design and coding required

Font styles to use
Sans Serif

Colors
59FF00
82FF00
B8FF75
E3FFCB
F4FFEA

Requirements
Must have
• eCommerce storefront, Made in USA references
Nice to have
• Home page, TREMLA Product page, About Us, Capabilities, Contact, etc.
Should not have
• Should not be too much text and reading.

```html
<!DOCTYPE html>
<html lang="en">
<head>
<meta charset="utf-8">
<title>Velk Manufacturing — Home of TREMLA</title>
<link rel="stylesheet" href="https://fonts.googleapis.com/css2?family=Saira+Semi+Expanded:wght@500;600;700&family=Nunito+Sans:wght@400;600&display=swap">
<style>
:root{
  --green:#2fa52f;
  --black:#000;
  --ink:#111;
  --white:#fff;
  --grey-band:#e4e5e7;
  --field:#3a3a3a;
  --field-text:#cfcfcf;
  --head:"Saira Semi Expanded",sans-serif;
  --body:"Nunito Sans",sans-serif;
}
*{margin:0;padding:0;box-sizing:border-box}
html,body{width:670px;height:1200px;overflow:hidden;background:var(--white)}
.page{position:relative;width:670px;height:1200px;overflow:hidden;font-family:var(--body);color:var(--ink)}
.abs{position:absolute}

/* header */
.brand{left:52px;top:8px;font-family:var(--head);font-weight:700;font-size:16px;letter-spacing:1px;color:var(--black);line-height:20px;white-space:nowrap}
.nav{left:290px;top:12px;font-family:var(--head);font-weight:600;font-size:6px;letter-spacing:.2px}
.nav a{position:absolute;top:0;white-space:nowrap;color:var(--ink);text-decoration:none}
.nav a.current{color:var(--green)}
.btn{display:flex;align-items:center;justify-content:center;font-family:var(--head);font-weight:600;font-size:6px;letter-spacing:.3px;color:var(--white);background:var(--green);border-radius:1px;white-space:nowrap;text-decoration:none}
.btn.dark{background:var(--black)}
.btn.outline{background:transparent;border:1px solid var(--white)}
.btn-header{left:555px;top:9px;width:62px;height:17px}

/* hero */
.hero{left:0;top:35px;width:670px;height:262px;background:radial-gradient(ellipse at 70% 30%,#5b5b5b 0%,#2f2f2f 45%,#161616 100%)}
.hero-shot{left:400px;top:67px;width:159px;height:196px;border-radius:8px;background:linear-gradient(150deg,#3fc63f 0%,#1f8e1f 55%,#8d8d8d 100%);opacity:.92}
.eyebrow{left:112px;top:99px;font-family:var(--head);font-weight:600;font-size:8px;color:var(--white);letter-spacing:.3px;white-space:nowrap}
.hero-title{left:112px;top:118px;font-family:var(--head);font-weight:700;font-size:16.5px;line-height:20.3px;color:var(--white);white-space:nowrap}
.btn-hero{left:112px;top:212px;width:56px;height:18px}
.btn-shop{left:174px;top:212px;width:66px;height:18px}

/* why */
.thumb{width:84px;height:66px;background:linear-gradient(135deg,#2b2b2b,#4a4a4a 60%,#2e8a2e)}
.thumb-a{left:112px;top:341px}
.thumb-b{left:112px;top:421px}
.why-shot{left:198px;top:331px;width:128px;height:167px;border-radius:8px;background:linear-gradient(160deg,#3dc23d 0%,#23982a 60%,#b3b3b3 100%)}
h2{font-family:var(--head);font-weight:600;font-size:13px;letter-spacing:.2px;color:var(--ink);position:absolute;white-space:nowrap}
.why-title{left:342px;top:358px}
.why-lead{left:342px;top:380px;width:222px;font-size:6px;line-height:7.8px}
.ticks{list-style:none;position:absolute;font-size:6.6px}
.ticks li{position:relative;padding-left:12px}
.ticks li::before{content:"→";position:absolute;left:0;top:0;color:var(--green);font-size:6px}
.why-ticks{left:342px;top:404px;line-height:10.5px}
.btn-why{left:342px;top:449px;width:56px;height:18px}

/* what we do */
.band{left:0;top:558px;width:670px;height:227px;background:var(--grey-band)}
.parts-shot{left:398px;top:530px;width:161px;height:220px;border-radius:2px;background:radial-gradient(circle at 40% 40%,#d8d8d8 0%,#9a9a9a 50%,#5e5445 100%)}
.what-title{left:112px;top:593px}
.what-copy{left:112px;top:617px;width:258px;font-size:6px;line-height:8.4px}
.what-copy p{margin-bottom:8.4px}
.btn-what{left:112px;top:729px;width:56px;height:18px}

/* better */
.better-title{left:135px;top:816px}
.better-shot{left:154px;top:847px;width:135px;height:133px;border-radius:8px;background:linear-gradient(135deg,#3cc03c 0%,#22902a 60%,#bdbdbd 100%)}
.better-ticks{left:342px;top:820px;width:215px;font-size:6px;line-height:8.4px}
.better-ticks li{margin-bottom:4.2px}
.btn-better{left:342px;top:965px;width:56px;height:18px}

/* footer */
.footer{left:0;top:1018px;width:670px;height:182px;background:var(--black);color:var(--white)}
.foot-brand{left:112px;top:1044px;font-family:var(--head);font-weight:700;font-size:17px;letter-spacing:1px;color:var(--white);white-space:nowrap}
.foot-mark{left:112px;top:1092px;font-family:var(--head);font-weight:600;font-size:9px;color:var(--white);display:flex;align-items:center;gap:5px;white-space:nowrap}
.foot-mark i{display:block;width:9px;height:9px;border-radius:50%;background:var(--green)}
.foot-h{position:absolute;font-family:var(--head);font-weight:600;font-size:6.5px;letter-spacing:.3px;color:var(--white);white-space:nowrap}
.foot-h.green{color:var(--green)}
.call{left:265px;top:1060px;font-family:var(--head);font-size:9px;color:var(--green);white-space:nowrap}
.mail{left:265px;top:1073px;font-family:var(--head);font-size:6.6px;color:var(--white)}
.addr{left:265px;top:1098px;font-family:var(--head);font-size:6.6px;line-height:8.5px;color:var(--white);white-space:nowrap}
.social{width:17px;height:17px;border-radius:50%;background:#ededed}
.social.on{background:var(--green)}
.field{background:var(--field);color:var(--field-text);font-size:5.5px;padding:4px 6px;border-radius:1px}
.rule{left:112px;top:1175px;width:446px;height:1px;background:#3a3a3a}
.copy{left:112px;top:1183px;font-family:var(--head);font-size:5.8px;color:var(--white);white-space:nowrap}
.copy span{color:var(--green)}
.foot-nav a{position:absolute;top:1183px;font-family:var(--head);font-size:6px;color:var(--white);text-decoration:none;white-space:nowrap}
.foot-nav a.current{color:var(--green)}
</style>
</head>
<body>
<div class="page">

  <!-- header -->
  <div class="abs brand">VELK MFG</div>
  <nav class="abs nav">
    <a class="current" style="left:0">-- HOME --</a>
    <a style="left:46px">CAPABILITIES</a>
    <a style="left:102px">ABOUT US</a>
    <a style="left:148px">GALLERY</a>
    <a style="left:188px">WISDOM</a>
    <a style="left:228px">SHOP</a>
  </nav>
  <a class="abs btn btn-header">CONTACT US</a>

  <!-- hero -->
  <section class="abs hero"></section>
  <div class="abs hero-shot" role="img" aria-label="Green anodized TREMLA tool with steel rod, floating over a blurred field of machined parts"></div>
  <svg class="abs" style="left:228px;top:26px" width="442" height="18" viewBox="0 0 442 18"><rect x="8" y="6" width="434" height="6" fill="#2fa52f"/><polygon points="0,9 10,0 10,18" fill="#2fa52f"/></svg>
  <div class="abs eyebrow">WELCOME TO VELK MANUFACTURING · MADE IN USA</div>
  <h1 class="abs hero-title">WE ARE A MACHINE SHOP<br>WITH COMPLETE END TO END<br>MANUFACTURING<br>CAPABILITIES.</h1>
  <a class="abs btn btn-hero">ABOUT US</a>
  <a class="abs btn outline btn-shop">SHOP TREMLA</a>
  <svg class="abs" style="left:0;top:287px" width="443" height="20" viewBox="0 0 443 20"><rect x="0" y="6" width="434" height="7" fill="#2fa52f"/><polygon points="432,0 443,9.5 432,19" fill="#2fa52f"/></svg>

  <!-- why -->
  <div class="abs thumb thumb-a" role="img" aria-label="TREMLA tool set in a foam case with hex key"></div>
  <div class="abs thumb thumb-b" role="img" aria-label="TREMLA tool and rod packed in a foam case"></div>
  <div class="abs why-shot" role="img" aria-label="Green TREMLA tool render with steel rod"></div>
  <h2 class="why-title">WHY VELK MANUFACTURING?</h2>
  <p class="abs why-lead">Because there is a better way, and we will find it, even if it's the hard way. We believe in working harder and smarter to achieve success.</p>
  <ul class="ticks why-ticks">
    <li>Our success is measured in your success</li>
    <li>Focused on our your needs and making excellent parts</li>
    <li>Exceeding your expectations</li>
  </ul>
  <a class="abs btn dark btn-why">CONTACT US</a>

  <!-- what we do -->
  <section class="abs band"></section>
  <svg class="abs" style="left:228px;top:549px" width="442" height="19" viewBox="0 0 442 19"><rect x="8" y="6" width="434" height="7" fill="#2fa52f"/><polygon points="0,9.5 10,0 10,19" fill="#2fa52f"/></svg>
  <div class="abs parts-shot" role="img" aria-label="Rows of machined aluminium parts on a tray"></div>
  <h2 class="what-title">WHAT WE DO</h2>
  <div class="abs what-copy">
    <p>We are a machine shop with complete end to end manufacturing capabilities. We can take an idea or need, and bring it to a complete physical product. We can design and build your prototype, and we can mass produce it too.</p>
    <p>We love working directly with customers to manufacture their products, and help make it better where appropriate. We can work with as little as a verbal description, up to following fully defined customer specifications.</p>
    <p>We work in a wide variety of materials, and are very good at creating fixture designs to address your process issues. We can even come to your business and help you make improvements onsite. We have helped many other machine shops be more successful.</p>
  </div>
  <a class="abs btn btn-what">CONTACT US</a>
  <svg class="abs" style="left:0;top:775px" width="443" height="20" viewBox="0 0 443 20"><rect x="0" y="6" width="434" height="7" fill="#2fa52f"/><polygon points="432,0 443,9.5 432,19" fill="#2fa52f"/></svg>

  <!-- better -->
  <h2 class="better-title">HOW WE MAKE IT BETTER</h2>
  <div class="abs better-shot" role="img" aria-label="Green TREMLA tool render at an angle"></div>
  <ul class="ticks better-ticks">
    <li>With 100 years of combined knowledge and experience to draw upon, we find solutions.</li>
    <li>Our vast experience across multiple industries gives us insight that is invaluable in creativity and foresight.</li>
    <li>This real life experience brings a broader understanding of what works, and more importantly, what doesn't work, ultimately allowing us to make more informed decisions.</li>
    <li>We consider the smallest details, and envision all the consequences in order to create a better product the first time.</li>
    <li>By recognizing risks early, we can address them before they become issues.</li>
    <li>We continuously improve and learn new things by staying up to date with emerging technologies and techniques.</li>
  </ul>
  <a class="abs btn dark btn-better">CONTACT US</a>

  <!-- footer -->
  <footer class="abs footer"></footer>
  <svg class="abs" style="left:228px;top:1008px" width="442" height="19" viewBox="0 0 442 19"><rect x="8" y="6" width="434" height="7" fill="#2fa52f"/><polygon points="0,9.5 10,0 10,19" fill="#2fa52f"/></svg>
  <div class="abs foot-brand">VELK MFG</div>
  <div class="abs foot-mark"><i></i>Made in USA</div>

  <div class="foot-h" style="left:265px;top:1046px">CONTACT US</div>
  <div class="abs call">Call: 555-014-2290</div>
  <div class="abs mail">info@velkmfg.com</div>
  <div class="foot-h green" style="left:265px;top:1090px">ADDRESS:</div>
  <div class="abs addr">Lorem ipsum work 195 N-4646<br>work design - 1234</div>
  <div class="foot-h green" style="left:265px;top:1132px">FOLLOW US</div>
  <div class="abs social" style="left:265px;top:1144px" aria-label="Social profile"></div>
  <div class="abs social on" style="left:286px;top:1144px" aria-label="Social profile"></div>
  <div class="abs social" style="left:307px;top:1144px" aria-label="Social profile"></div>

  <div class="foot-h" style="left:401px;top:1046px">SEND US MESSAGE</div>
  <div class="abs field" style="left:401px;top:1063px;width:75px;height:14px">Name</div>
  <div class="abs field" style="left:483px;top:1063px;width:75px;height:14px">Phone</div>
  <div class="abs field" style="left:401px;top:1084px;width:157px;height:14px">Email</div>
  <div class="abs field" style="left:401px;top:1105px;width:157px;height:31px">Message</div>
  <a class="abs btn" style="left:401px;top:1143px;width:49px;height:17px">SEND</a>

  <div class="abs rule"></div>
  <div class="abs copy">© 2022 <span>Velk Manufacturing.</span> All Right Reserved</div>
  <nav class="foot-nav">
    <a class="current" style="left:265px">– Home –</a>
    <a style="left:307px">Capabilities</a>
    <a style="left:350px">About Us</a>
    <a style="left:386px">Gallery</a>
    <a style="left:417px">Wisdom</a>
    <a style="left:450px">Shop</a>
    <a style="left:474px">Contact Us</a>
  </nav>
  <svg class="abs" style="left:572px;top:1169px" width="11" height="13" viewBox="0 0 11 13"><polyline points="1,12 5.5,1 10,12 5.5,8 1,12" fill="none" stroke="#2fa52f" stroke-width="1.3" stroke-linejoin="round"/></svg>
</div>
</body>
</html>
```